Web Design Project for Brantley Harbor Advisors, LP

We are looking for a new website for Brantley Harbor Advisors, LP an investment management (alternative investment) firm with offices in New York, NY and Seattle, WA. We are looking for designs utilizing gray, blue and white, corresponding with our logo. Our current website is www.brantleyharborllc.example.

Some websites with the feel we are looking for:

http://quillbrookfunds.example/cgi-bin/index.pl
http://www.tessendalp.example/

Target Market(s)

wealthy individuals and large investors

Industry/Entity Type

Investment

Requirements
Must have
• A couple/few page website, utilizing the below text & contact info and use one of the logos that are attached.

Text to be inlcuded:

Brantley Harbor Advisors, LP is a hedge fund manager responsible for a multi-strategy fund primarily implementing a long/short equity strategy and utilizing macro, credit, event driven and distressed strategies while maintaining a market neutral portfolio.

The Fund seeks to achieve absolute returns while minimizing risk with particular attention paid to preserving capital.

Contact information to be included:

East Coast:

417 Corwin Street #608
New York, NY 10093
Phone : +1 212.555.0147
Fax : +1 212.555.0183
info@brantleyharborllc.example

West Coast:

3871 Halvern Street #524
Seattle, WA 98190
info@brantleyharborllc.example
Should not have
• anything too flashy

```html
<!DOCTYPE html>
<html lang="en">
<head>
<meta charset="utf-8">
<title>Brantley Harbor Advisors, LP</title>
<link rel="stylesheet" href="https://fonts.googleapis.com/css2?family=PT+Sans:wght@400;700&family=PT+Sans+Narrow:wght@400;700&family=Source+Sans+3:wght@400;600&display=swap">
<style>
  :root {
    --page-gray: #4a4a4a;
    --brand-blue: #003278;
    --brand-blue-bright: #0a4eb0;
    --heading-blue: #0c4aa0;
    --body-gray: #a3a3a3;
    --panel-gray: #ececec;
    --rule-gray: #c9c9c9;
    --white: #ffffff;
    --footer-gray: #7a7a7a;
  }
  * { margin: 0; padding: 0; box-sizing: border-box; }
  html, body { width: 1200px; height: 1028px; overflow: hidden; }
  body { background: var(--page-gray); font-family: "Source Sans 3", sans-serif; }

  .site { position: absolute; left: 120px; top: 0; width: 960px; height: 1028px; background: #fdfdfd; }

  .masthead { position: absolute; left: 0; top: 18px; width: 960px; height: 152px; background: var(--brand-blue); overflow: hidden; }
  .masthead-shade { position: absolute; left: 0; top: 0; width: 960px; height: 152px;
    background: linear-gradient(100deg, rgba(10,78,176,0) 55%, rgba(10,78,176,0.55) 85%, rgba(10,78,176,0.8) 100%); }
  .brand-name { position: absolute; left: 30px; top: 56px; font-family: "PT Sans", sans-serif; font-weight: 400; font-size: 38px; line-height: 44px; color: var(--white); letter-spacing: 1px; }

  .masthead-rule { position: absolute; left: 0; top: 170px; width: 960px; height: 4px; background: var(--white); }

  .main-nav { position: absolute; left: 0; top: 174px; width: 960px; height: 35px; background: var(--brand-blue); }
  .main-nav ul { list-style: none; display: flex; align-items: center; position: absolute; left: 36px; top: 6px; }
  .main-nav li { font-family: "PT Sans Narrow", sans-serif; font-weight: 700; font-size: 18px; color: var(--white); letter-spacing: 0.5px; }
  .main-nav .current { border-bottom: 3px solid var(--white); line-height: 22px; position: relative; }
  .main-nav .current::before { content: ""; position: absolute; left: 0; right: 0; top: -7px; height: 5px; background: var(--white); }
  .main-nav .sep { margin: 0 11px; }

  .hero { position: absolute; left: 0; top: 209px; width: 960px; height: 301px;
    background: linear-gradient(160deg, #e8eef6 0%, #c4d2e6 40%, #8aa3c8 70%, #d9e3ef 100%); }

  .content-area { position: absolute; left: 0; top: 510px; width: 960px; height: 358px; background: var(--panel-gray); }

  .about-card { position: absolute; left: 83px; top: 455px; width: 802px; height: 365px;
    background: linear-gradient(#fdfdfd, #f6f6f6); border: 1px solid #d6d6d6; }
  .about-card h1 { position: absolute; left: 43px; top: 26px; font-family: "PT Sans", sans-serif; font-weight: 700; font-size: 25px; color: var(--heading-blue); letter-spacing: 0.5px; }
  .about-card hr { position: absolute; left: 19px; top: 68px; width: 770px; border: 0; border-top: 1px solid var(--rule-gray); }
  .about-card .copy { position: absolute; left: 42px; top: 92px; width: 726px; }
  .about-card p { font-weight: 600; font-size: 18.5px; line-height: 30px; color: var(--body-gray); margin-bottom: 30px; }

  .site-footer { position: absolute; left: 0; top: 868px; width: 960px; height: 129px; background: var(--brand-blue); font-family: "PT Sans Narrow", sans-serif; color: var(--white); }
  .footer-col { position: absolute; top: 24px; }
  .footer-col h2 { font-size: 14px; font-weight: 700; letter-spacing: 0.3px; margin-bottom: 5px; }
  .footer-col ul { list-style: none; }
  .footer-col li { font-size: 11.5px; font-weight: 700; line-height: 14px; }
  .footer-col.follow li { line-height: 18px; font-size: 11px; }

  .legal-line { position: absolute; left: 0; top: 1008px; width: 960px; text-align: center; font-family: "PT Sans", sans-serif; font-weight: 700; font-size: 10px; color: var(--footer-gray); letter-spacing: 0.3px; }
  .legal-line span { margin: 0 4px; }
</style>
</head>
<body>
<div class="site">
  <header class="masthead">
    <div class="masthead-shade" role="img" aria-label="Decorative blue curved bands on the right of the header"></div>
    <div class="brand-name">Brantley Harbor Advisors, LP</div>
  </header>
  <div class="masthead-rule"></div>

  <nav class="main-nav">
    <ul>
      <li class="current">HOME</li>
      <li class="sep">|</li>
      <li>CONTACT US</li>
    </ul>
  </nav>

  <div class="hero" role="img" aria-label="Close-up photo of a pen resting on a printed financial report with bar charts, in pale blue tones"></div>
  <div class="content-area"></div>

  <section class="about-card">
    <h1>About Us</h1>
    <hr>
    <div class="copy">
      <p>Brantley Harbor Advisors, LP is a hedge fund manager responsible for a multi-strategy fund primarily implementing a long/short equity strategy and utilizing macro, credit, event driven and distressed strategies while maintaining a market neutral portfolio.</p>
      <p>The Fund seeks to achieve absolute returns while minimizing risk with particular attention paid to preserving capital.</p>
    </div>
  </section>

  <footer class="site-footer">
    <div class="footer-col" style="left:83px"><h2>Other Services</h2><ul><li>Manage</li><li>Confidential Reports</li><li>Legal</li><li>On Hand</li></ul></div>
    <div class="footer-col" style="left:237px"><h2>Other Services</h2><ul><li>Manage</li><li>Confidential Reports</li><li>Legal</li><li>On Hand</li></ul></div>
    <div class="footer-col" style="left:399px"><h2>Other Services</h2><ul><li>Manage</li><li>Confidential Reports</li><li>Legal</li><li>On Hand</li></ul></div>
    <div class="footer-col" style="left:558px"><h2>Other Services</h2><ul><li>Manage</li><li>Confidential Reports</li><li>Legal</li><li>On Hand</li></ul></div>
    <div class="footer-col follow" style="left:726px"><h2>FOLLOW US:</h2><ul><li>www.socialpage.example/brantleyharbor/</li><li>www.socialpage.example/brantleyharbor/</li><li>www.socialpage.example/brantleyharbor/</li></ul></div>
  </footer>

  <div class="legal-line"><span>Copyright by: Harbor Studio</span> <span>Year: 2012</span> <span>Powered by: Me</span></div>
</div>
</body>
</html>
```